IT Services company general flyer

Looking for a printable US letter size flyer to give a brief overview of the services we offer. We also partner with another company for their services as well. Please check out our website at www.gizmobykellan.com and click on "Our Services" to learn about our services and visit www.bluefernguard,com and click on services to learn about their services. Several of our services do overlap, so they only need to be on the flyer once. Let me know if this is too much content and we need to weed some out. We do not want Home phone service on this flyer. The basic design of the flyer should mimic similar to the VOIP one you did for me for the colors and logo. Also check out the "Who Choose us" page on www.gizmobykellan.com to include some of that as well.

Target Market(s)

Targeting Small businesses that may not normally have a budget for their IT Services

Industry/Entity Type

It Service

Font styles to use
Serif
Sans Serif

Requirements
Must have
• Must include my logo, phone number and email/website address and must follow the same basic template of my previous flyers.

```html
<!DOCTYPE html>
<html lang="en">
<head>
<meta charset="utf-8">
<title>Gizmo By Kellan – IT Consulting &amp; Services</title>
<link rel="stylesheet" href="https://fonts.googleapis.com/css2?family=Josefin+Sans:wght@400;600;700&display=swap">
<style>
  :root {
    --red: #c0272d;
    --navy: #1d3a6e;
    --navy-deep: #132a55;
    --ink: #1c1c1f;
    --white: #ffffff;
    --grey: #e6e6e6;
  }
  * { margin: 0; padding: 0; box-sizing: border-box; }
  html, body { width: 800px; height: 1200px; overflow: hidden; background: var(--grey); }
  body { font-family: "Josefin Sans", sans-serif; color: var(--ink); }
  .flyer { position: relative; width: 800px; height: 1200px; background: var(--white); overflow: hidden; }
  .abs { position: absolute; }

  .hero-art { left: 0; top: 0; }
  .brand { left: 36px; top: 64px; display: flex; align-items: center; gap: 10px; }
  .brand-dot { width: 30px; height: 30px; border-radius: 50%; background: var(--navy); flex: none; }
  .brand-name { font-weight: 700; font-size: 23px; color: var(--navy); letter-spacing: 0.4px; line-height: 1; white-space: nowrap; }

  .title { left: 36px; top: 172px; font-weight: 600; font-size: 40px; line-height: 1.17; letter-spacing: 0.5px; }
  .title .line-red { color: var(--red); display: block; }
  .title .line-navy { color: var(--navy); font-weight: 700; display: block; }
  .title-rule { left: 36px; top: 270px; width: 236px; height: 2px; background: var(--navy); }
  .title-rule::before { content: ""; position: absolute; left: 22px; top: -2px; width: 56px; height: 5px; background: var(--red); }

  .intro { left: 36px; top: 306px; width: 270px; font-size: 12.4px; line-height: 1.32; color: var(--ink); }

  .section-head { font-weight: 700; font-size: 24px; letter-spacing: 0.5px; white-space: nowrap; }
  .section-head .accent { color: var(--red); }
  .section-head .base { color: var(--navy); }
  .services-head { left: 36px; top: 488px; }

  .service-list { list-style: none; }
  .service-list li { display: flex; align-items: center; height: 41px; font-size: 15px; font-weight: 600; color: var(--ink); white-space: nowrap; }
  .service-list svg { width: 18px; height: 18px; margin-right: 10px; flex: none; }
  .services-left { left: 36px; top: 514px; }
  .services-right { left: 428px; top: 514px; }

  .why-head { left: 38px; top: 752px; z-index: 2; }
  .why-band { left: 0; top: 0; }

  .reason { width: 210px; text-align: center; color: var(--white); }
  .reason h3 { font-size: 13.5px; font-weight: 600; line-height: 1.1; height: 30px; display: flex; align-items: flex-end; justify-content: center; }
  .reason p { margin-top: 8px; font-size: 11.4px; line-height: 1.26; }
  .reason-1 { left: 33px; top: 884px; }
  .reason-2 { left: 295px; top: 884px; }
  .reason-3 { left: 559px; top: 884px; }

  .call { left: 36px; top: 1114px; color: var(--white); font-weight: 700; white-space: nowrap; }
  .call-label { font-size: 25px; letter-spacing: 0.5px; line-height: 1; }
  .call-number { font-size: 35px; line-height: 1.15; }

  .contact { top: 1148px; display: flex; align-items: center; gap: 8px; font-size: 13.5px; font-weight: 600; color: var(--white); white-space: nowrap; }
  .contact svg { width: 13px; height: 13px; }
  .contact-email { left: 336px; }
  .contact-web { left: 582px; }
  .contact-divider { left: 560px; top: 1138px; width: 2px; height: 34px; background: var(--white); }
</style>
</head>
<body>
<main class="flyer">

  <svg class="abs hero-art" width="800" height="470" viewBox="0 0 800 470">
    <defs>
      <linearGradient id="heroTones" x1="0" y1="0" x2="1" y2="1">
        <stop offset="0" stop-color="#c9ced8"/>
        <stop offset="0.45" stop-color="#2f4c80"/>
        <stop offset="1" stop-color="#e4e7ec"/>
      </linearGradient>
    </defs>
    <polygon points="308,0 346,0 412,156 322,466 316,466 398,156" fill="var(--red)"/>
    <polygon points="340,0 800,0 800,466 324,466 412,156" fill="url(#heroTones)" role="img" aria-label="Photo of a businessman touching a digital security shield above a tablet"/>
  </svg>

  <div class="abs brand">
    <span class="brand-dot"></span>
    <span class="brand-name">GIZMO BY KELLAN</span>
  </div>

  <h1 class="abs title">
    <span class="line-red">IT CONSULTING</span>
    <span class="line-navy">&amp; SERVICES</span>
  </h1>
  <div class="abs title-rule"></div>

  <p class="abs intro">At Gizmo By Kellan, we provide complete managed IT services tailored for your small and medium business. We understand small business because we are small business. We can help bring enterprise technology solutions to your small business</p>

  <h2 class="abs section-head services-head"><span class="accent">OUR</span> <span class="base">SERVICES</span></h2>

  <ul class="abs service-list services-left">
    <li><svg viewBox="0 0 18 18" fill="none" stroke="var(--red)" stroke-width="1.4"><path d="M4 13h10a3 3 0 0 0 0-6 4.5 4.5 0 0 0-8.6-1A3.5 3.5 0 0 0 4 13z"/></svg>Managed IT Services</li>
    <li><svg viewBox="0 0 18 18" fill="none" stroke="var(--red)" stroke-width="1.4"><path d="M5 2l3 3-2 2a9 9 0 0 0 5 5l2-2 3 3-2 3C8 16 2 10 2 4z"/></svg>Business VOIP Phone Service</li>
    <li><svg viewBox="0 0 18 18" fill="none" stroke="var(--red)" stroke-width="1.4"><rect x="2" y="2" width="6" height="5"/><rect x="10" y="2" width="6" height="5"/><rect x="6" y="11" width="6" height="5"/><path d="M5 7v2h8V7M9 9v2"/></svg>Network Security</li>
    <li><svg viewBox="0 0 18 18" fill="none" stroke="var(--red)" stroke-width="1.4"><path d="M3 6a8.5 8.5 0 0 1 12 0M5.5 9a5 5 0 0 1 7 0"/><circle cx="9" cy="12.5" r="1.4"/></svg>Wireless Solutions</li>
    <li><svg viewBox="0 0 18 18" fill="none" stroke="var(--red)" stroke-width="1.4"><rect x="2" y="3" width="14" height="10"/><path d="M6 16h6M9 13v3M6 10h6a2 2 0 0 0 0-4 3 3 0 0 0-6 1z"/></svg>Cloud Services</li>
  </ul>

  <ul class="abs service-list services-right">
    <li><svg viewBox="0 0 18 18" fill="none" stroke="var(--red)" stroke-width="1.4"><rect x="2" y="3" width="14" height="12"/><path d="M2 6h14M5 9h8M5 12h5"/></svg>Business Office Apps Service</li>
    <li><svg viewBox="0 0 18 18" fill="none" stroke="var(--red)" stroke-width="1.4"><rect x="2" y="3" width="14" height="9"/><path d="M6 16h6M9 12v4"/><path d="M9 5l2.5 1v2c0 1.5-1.2 2.3-2.5 2.8C7.7 10.3 6.5 9.5 6.5 8V6z"/></svg>Endpoint Security Services</li>
    <li><svg viewBox="0 0 18 18" fill="none" stroke="var(--red)" stroke-width="1.4"><ellipse cx="8" cy="4" rx="5" ry="2"/><path d="M3 4v9c0 1 2 2 5 2M13 4v4M3 8.5c0 1 2 2 5 2"/><path d="M11 12a3 3 0 1 0 3-2.6M14 8v2h-2"/></svg>Backup &amp; Disaster Recovery Services</li>
    <li><svg viewBox="0 0 18 18" fill="none" stroke="var(--red)" stroke-width="1.4"><circle cx="9" cy="9" r="5"/><circle cx="9" cy="9" r="2"/><path d="M9 1v3M9 14v3M1 9h3M14 9h3"/></svg>Cyber Security Assessment Services</li>
    <li><svg viewBox="0 0 18 18" fill="none" stroke="var(--red)" stroke-width="1.4"><rect x="4" y="8" width="10" height="8"/><path d="M6 8V5a3 3 0 0 1 6 0v3"/><circle cx="9" cy="12" r="1.2"/></svg>Ransomware &amp; Threat Response Services</li>
  </ul>

  <svg class="abs why-band" width="800" height="1200" viewBox="0 0 800 1200">
    <defs>
      <linearGradient id="bandTones" x1="0" y1="0" x2="1" y2="1">
        <stop offset="0" stop-color="var(--navy-deep)"/>
        <stop offset="0.55" stop-color="var(--navy)"/>
        <stop offset="1" stop-color="#22457f"/>
      </linearGradient>
    </defs>
    <polygon points="0,784 268,784 292,748 800,748 800,1078 0,1078" fill="url(#bandTones)" role="img" aria-label="Faint backdrop of business people at a keyboard in navy tones"/>
    <line x1="138" y1="842" x2="664" y2="842" stroke="var(--white)" stroke-width="1" stroke-dasharray="4 3" opacity="0.8"/>
    <g fill="var(--white)">
      <circle cx="138" cy="842" r="34"/>
      <circle cx="400" cy="842" r="34"/>
      <circle cx="664" cy="842" r="34"/>
    </g>
    <g fill="none" stroke="var(--red)" stroke-width="1.6">
      <path d="M126 846v-6a12 12 0 0 1 24 0v6"/><rect x="122" y="844" width="6" height="9" rx="2"/><rect x="148" y="844" width="6" height="9" rx="2"/><path d="M151 853c0 4-5 6-10 6"/>
      <path d="M388 858v-10h8v10M384 858h26M404 848v-16M399 837l5-5 5 5"/><circle cx="392" cy="842" r="3"/>
      <circle cx="664" cy="836" r="8"/><path d="M660 848h8M661 852h6M664 822v-4M654 826l-3-3M674 826l3-3M648 858h20l6-4"/>
    </g>
    <polygon points="0,1094 324,1094 312,1200 0,1200" fill="var(--red)"/>
    <polygon points="324,1119 800,1119 800,1200 312,1200" fill="var(--ink)"/>
  </svg>

  <h2 class="abs section-head why-head"><span class="accent">WHY</span> <span class="base">CHOOSE US</span></h2>

  <div class="abs reason reason-1">
    <h3>Personalized<br>Solutions &amp; Support</h3>
    <p>We know your time is valuable and your technology is critical. That's why we take time to visit with each of our clients and recommend the best solution for them. Your not just another client to us, we want what is best for you.</p>
  </div>
  <div class="abs reason reason-2">
    <h3>Experience</h3>
    <p>We have years of experience in both large and small environments. We know what solutions are available and how to implement them in your business. We are constantly working with industry experts with today's changing technology.</p>
  </div>
  <div class="abs reason reason-3">
    <h3>One Stop Shop</h3>
    <p>We can help you with all your IT needs, weather it be computer or network security. Phone and Voice needs, or cloud services. Contact us today to discuss how we can help you.</p>
  </div>

  <div class="abs call">
    <div class="call-label">CALL US NOW!</div>
    <div class="call-number">555-014-0199</div>
  </div>

  <div class="abs contact contact-email">
    <svg viewBox="0 0 13 13"><rect x="0.5" y="2.5" width="12" height="8" fill="var(--red)"/><path d="M0.5 2.5l6 4.5 6-4.5" fill="none" stroke="var(--white)" stroke-width="1"/></svg>
    <span>info@gizmobykellan.com</span>
  </div>
  <div class="abs contact-divider"></div>
  <div class="abs contact contact-web">
    <svg viewBox="0 0 13 13" fill="none" stroke="var(--red)" stroke-width="1.2"><circle cx="6.5" cy="6.5" r="5.8"/><ellipse cx="6.5" cy="6.5" rx="2.6" ry="5.8"/><path d="M0.7 6.5h11.6"/></svg>
    <span>www.gizmobykellan.com</span>
  </div>

</main>
</body>
</html>
```